continued... Web Design for Professional Development and marketplace

in addition to the homepages that you are desiging, can you also create designs for the attached wireframes that are part of the same website.
I am creating this as a seperate project as we are keen to see your designs for the rest of the website.
VIdeo of prototype and homepage designs
https://www.filquarry.net/sh/qm7rtp2vbx9kka3/J2wNo8LpXe/design
Updates
added an additional wireframe that was missed in the original upload
added one more wireframe for the homepage: where the user is prompted to login or signup
Industry/Entity Type
Marketplace
Look and feel
Each slider illustrates characteristics of the customer's brand and the style your logo design should communicate.

```html
<!DOCTYPE html>
<html lang="en">
<head>
<meta charset="utf-8">
<title>Marketplace – Marketing Courses</title>
<link rel="stylesheet" href="https://fonts.googleapis.com/css2?family=Open+Sans:wght@400;600;700&display=swap">
<style>
:root{
  --blue-top:#1d8bd0;
  --blue-bottom:#0a5893;
  --blue-text:#1b5d8d;
  --dark-top:#5d5d5d;
  --dark-bottom:#2b2b2b;
  --page:#e8e8e8;
  --white:#ffffff;
  --ink:#333333;
  --muted:#555555;
  --line:#d4d4d4;
  --star:#f2b705;
  --heart:#d8262b;
  --tick:#5a9a1f;
  --icon:#3c3c3c;
}
*{box-sizing:border-box;margin:0;padding:0}
html,body{width:1200px;height:1009px;overflow:hidden}
body{background:var(--page);font-family:"Open Sans",Arial,sans-serif;color:var(--ink);position:relative}
.abs{position:absolute}

/* header */
.site-header{position:absolute;left:0;top:0;width:1200px;height:75px;background:linear-gradient(var(--blue-top),var(--blue-bottom))}
.menu-toggle{left:116px;top:15px;width:46px;height:46px;border-radius:6px;background:linear-gradient(#3a3a3a,#050505);border:1px solid #6a9cc4}
.menu-toggle span{position:absolute;left:8px;width:28px;height:2px;background:var(--white)}
.search-field{left:205px;top:18px;width:240px;height:40px;border-radius:20px;background:var(--white);border:2px solid #c9dbe9;padding-left:12px;font-size:18px;line-height:36px;color:#888}
.header-btn{top:18px;height:40px;border-radius:5px;background:var(--white);border:3px solid #0d5f9b;box-shadow:0 0 0 1px #fff;display:flex;align-items:center;justify-content:center;gap:8px;font-size:15px;color:#0d4f86;letter-spacing:.4px}
.signup-link{left:998px;top:26px;font-size:18px;color:var(--white);letter-spacing:.4px}

/* secondary links */
.info-bar{left:0;top:75px;width:1200px;height:42px;background:var(--white)}
.info-bar a{position:absolute;top:14px;font-size:13px;color:#222;text-decoration:none}

/* filter bar */
.filter-bar{left:0;top:117px;width:1200px;height:59px;background:linear-gradient(var(--dark-top),var(--dark-bottom))}
.filter{position:absolute;top:0;height:59px;border-right:1px solid #1f1f1f;box-shadow:1px 0 0 #6b6b6b;color:var(--white);text-align:center}
.filter .label{display:block;font-size:17px;margin-top:10px;letter-spacing:.3px}
.filter .value{display:block;font-size:12px;margin-top:1px}
.caret{display:inline-block;width:0;height:0;border-left:5px solid transparent;border-right:5px solid transparent;border-top:6px solid var(--white);vertical-align:middle;margin-left:8px}

/* login panel */
.login-panel{left:101px;top:200px;width:998px;height:229px;background:var(--white);border:1px solid #d8d8d8;border-radius:6px;box-shadow:0 8px 10px -6px rgba(0,0,0,.25)}
.login-title{left:51px;top:28px;font-size:24px;color:var(--blue-text);letter-spacing:1.2px}
.prolink-btn{left:51px;top:77px;width:383px;height:42px;border-radius:4px;background:linear-gradient(#5bb2d9,#2d8ec0);border-bottom:2px solid #1d6f9a;color:var(--white);font-size:22px;letter-spacing:.8px;display:flex;align-items:center;padding-left:20px;gap:14px}
.prolink-btn .mark{width:14px;height:14px;background:var(--white)}
.divider{left:519px;top:35px;height:111px;border-left:1px dotted #999}
.text-input{left:589px;width:319px;height:34px;border-radius:17px;background:linear-gradient(#e4e4e4,#fafafa);border:2px solid #cfcfcf;font-size:13px;color:#444;padding-left:15px;line-height:30px}
.signin-btn{left:795px;top:152px;width:111px;height:29px;border-radius:8px;background:linear-gradient(#2d97d6,#0b5c99);color:var(--white);font-size:17px;text-align:center;line-height:28px;letter-spacing:.5px}
.create-account{left:0;width:998px;top:180px;text-align:center;font-size:18px;letter-spacing:.6px;color:#222}

/* listing */
.section-title{left:109px;top:459px;font-size:24px;color:var(--blue-text);letter-spacing:1px}
.dark-btn{background:linear-gradient(#6a6a6a,#1f1f1f);border:1px solid #111;border-radius:4px;color:var(--white)}
.sort-btn{left:106px;top:501px;width:149px;height:52px}
.sort-btn .label{position:absolute;left:29px;top:3px;font-size:17px}
.sort-btn .value{position:absolute;left:25px;top:27px;font-size:14px}
.view-toggle{left:917px;top:499px;width:179px;height:52px;display:flex}
.view-toggle div{flex:1;display:flex;align-items:center;justify-content:center;gap:8px;font-size:19px;letter-spacing:.5px}
.view-toggle div+div{border-left:1px solid #111;box-shadow:inset 1px 0 0 #777}

.add-tile{left:101px;top:579px;width:233px;height:208px;border-radius:8px;background:linear-gradient(#1a8ad0,#0a5891);color:var(--white);text-align:center}
.add-tile h3{font-weight:400;font-size:22px;margin-top:24px;letter-spacing:.6px}

.course-card{top:581px;width:232px;height:347px;border-radius:7px;background:linear-gradient(#ffffff,#ececec);border:1px solid #d3d3d3;box-shadow:0 8px 10px -6px rgba(0,0,0,.3)}
.provider-logo{position:absolute;left:13px;top:14px;width:206px;height:78px;border:4px solid #c9c9c9;background:var(--white);display:flex;align-items:center;justify-content:center;gap:8px;font-size:16px;font-weight:600;color:#1c1c4a;text-align:center;line-height:1.15}
.provider-logo .mark{width:14px;height:14px;background:#1c1c4a;flex:none}
.course-title{position:absolute;left:16px;top:97px;font-size:16px;font-weight:700;color:var(--blue-text);letter-spacing:1.3px;line-height:22px}
.course-provider{position:absolute;right:15px;top:136px;font-size:13px;color:#444;letter-spacing:.3px}
.stars{position:absolute;left:33px;top:166px}
.formats{position:absolute;right:16px;top:210px;display:flex;gap:14px}
.price{position:absolute;right:18px;top:259px;font-size:20px;font-weight:700;color:var(--blue-text);letter-spacing:1px}
.badge{position:absolute;left:16px;top:238px}
.register-tab{position:absolute;left:43px;top:319px}
</style>
</head>
<body>

<header class="site-header">
  <div class="abs menu-toggle"><span style="top:13px"></span><span style="top:21px"></span><span style="top:29px"></span></div>
  <div class="abs search-field">search</div>
  <div class="abs header-btn" style="left:688px;width:150px">
    <svg width="22" height="22" viewBox="0 0 22 22"><circle cx="8" cy="6" r="5" fill="#222"/><path d="M0 21c0-7 3-9 8-9s8 2 8 9z" fill="#222"/><circle cx="16" cy="16" r="5" fill="#222" stroke="#fff" stroke-width="1.5"/><path d="M16 13v6M13 16h6" stroke="#fff" stroke-width="1.6"/></svg>
    Add Review
  </div>
  <div class="abs header-btn" style="left:868px;width:100px">
    <svg width="18" height="18" viewBox="0 0 18 18"><circle cx="9" cy="5" r="4.5" fill="#222"/><path d="M0 18c0-6 4-8 9-8s9 2 9 8z" fill="#222"/></svg>
    Login
  </div>
  <div class="abs signup-link">Sign Up</div>
</header>

<nav class="abs info-bar">
  <a href="#" style="left:538px">About</a>
  <a href="#" style="left:613px">Business</a>
  <a href="#" style="left:708px">Developers</a>
  <a href="#" style="left:816px">Privacy &amp; Terms</a>
  <a href="#" style="left:954px">Copyright &amp; Trademark</a>
</nav>

<nav class="abs filter-bar">
  <div class="filter" style="left:98px;width:99px"><span class="label">Save</span>
    <svg width="24" height="16" viewBox="0 0 24 16" style="margin-top:1px"><path d="M2 6h8V0h4v6h8v4h-8v6h-4v-6H2z" fill="#fff"/></svg></div>
  <div class="filter" style="left:197px;width:99px"><span class="label">Career<i class="caret"></i></span><span class="value">(All)</span></div>
  <div class="filter" style="left:296px;width:159px"><span class="label">Specialization<i class="caret"></i></span><span class="value">(All)</span></div>
  <div class="filter" style="left:455px;width:126px"><span class="label">Location<i class="caret"></i></span><span class="value">(Vancouver)</span></div>
  <div class="filter" style="left:581px;width:102px"><span class="label">Price<i class="caret"></i></span><span class="value">($600-$3000)</span></div>
  <div class="filter" style="left:683px;width:125px"><span class="label">Start Date<i class="caret"></i></span><span class="value">(2-3 Months)</span></div>
  <div class="filter" style="left:808px;width:138px"><span class="label">Level Type<i class="caret"></i></span><span class="value">(intermediate)</span></div>
  <div class="filter" style="left:946px;width:89px;border-right:none;box-shadow:none"><span class="label">Provider<i class="caret"></i></span><span class="value">(One)</span></div>
</nav>

<section class="abs login-panel">
  <h2 class="abs login-title" style="font-weight:400">Save your search by logging in now</h2>
  <div class="abs prolink-btn"><span class="mark"></span>Sign in with ProLink</div>
  <div class="abs divider"></div>
  <div class="abs text-input" style="top:46px">First Name</div>
  <div class="abs text-input" style="top:100px">Last Name</div>
  <div class="abs signin-btn">Sign In</div>
  <p class="abs create-account">Or, Create account...</p>
</section>

<h2 class="abs section-title" style="font-weight:400">MARKETING</h2>
<div class="abs dark-btn sort-btn"><span class="label">Sort<i class="caret"></i></span><span class="value">(Trending)</span></div>
<div class="abs dark-btn view-toggle">
  <div><svg width="19" height="19" viewBox="0 0 19 19" fill="#fff"><rect width="8.5" height="8.5"/><rect x="10.5" width="8.5" height="8.5"/><rect y="10.5" width="8.5" height="8.5"/><rect x="10.5" y="10.5" width="8.5" height="8.5"/></svg>Grid</div>
  <div><svg width="25" height="20" viewBox="0 0 25 20" fill="#fff"><rect width="5" height="4"/><rect x="7" width="18" height="4"/><rect y="8" width="5" height="4"/><rect x="7" y="8" width="18" height="4"/><rect y="16" width="5" height="4"/><rect x="7" y="16" width="18" height="4"/></svg>List</div>
</div>

<div class="abs add-tile">
  <h3>Add Review</h3>
  <svg width="100" height="96" viewBox="0 0 100 96" style="margin-top:13px"><path d="M33 0h34v31h33v34H67v31H33V65H0V31h33z" fill="#fff"/></svg>
</div>

<!-- shared icon definitions -->
<svg width="0" height="0" style="position:absolute">
  <defs>
    <linearGradient id="starFill" x1="0" y1="0" x2="0" y2="1"><stop offset="0" stop-color="#ffe45c"/><stop offset="1" stop-color="#e8a200"/></linearGradient>
    <linearGradient id="starEmpty" x1="0" y1="0" x2="0" y2="1"><stop offset="0" stop-color="#ffffff"/><stop offset="1" stop-color="#d9d9d9"/></linearGradient>
    <linearGradient id="heartFill" x1="0" y1="0" x2="0" y2="1"><stop offset="0" stop-color="#ff6a6a"/><stop offset="1" stop-color="#b3141a"/></linearGradient>
    <linearGradient id="tabFill" x1="0" y1="0" x2="0" y2="1"><stop offset="0" stop-color="#2a97d8"/><stop offset="1" stop-color="#0a5791"/></linearGradient>
    <path id="star" d="M12 1l3.2 7 7.6.8-5.7 5.1 1.6 7.5L12 17.6l-6.7 3.8 1.6-7.5L1.2 8.8 8.8 8z"/>
    <g id="people" fill="#3c3c3c">
      <circle cx="24" cy="8" r="7"/><path d="M11 30c0-9 5-13 13-13s13 4 13 13z"/>
      <circle cx="10" cy="10" r="5.5"/><path d="M0 27c0-7 3-10 9-10 2 0 3 .3 4 .8-2 2-3 5-3 9.2z"/>
      <circle cx="38" cy="10" r="5.5"/><path d="M48 27c0-7-3-10-9-10-2 0-3 .3-4 .8 2 2 3 5 3 9.2z"/>
    </g>
    <path id="heart" d="M24 42C8 31 2 24 2 15 2 8 7 3 14 3c5 0 8 3 10 6 2-3 5-6 10-6 7 0 12 5 12 12 0 9-6 16-22 27z" fill="url(#heartFill)" stroke="#9c1014" stroke-width="1"/>
    <g id="registerTab">
      <path d="M0 18h14v11H0z M130 18h16v11h-16z" fill="#2b2b2b"/>
      <path d="M18 0h110l12 30c-1 4-3 5-6 5H12c-3 0-5-1-6-5z" fill="url(#tabFill)"/>
    </g>
  </defs>
</svg>

<article class="abs course-card" style="left:355px">
  <div class="provider-logo"><span class="mark"></span>Meridian<br>Marketing</div>
  <h3 class="course-title">Product Management<br>Focus</h3>
  <p class="course-provider">Meridian Marketing</p>
  <svg class="stars" width="150" height="24" viewBox="0 0 150 24"><use href="#star" fill="url(#starFill)" stroke="#c98a00"/><use href="#star" x="31" fill="url(#starFill)" stroke="#c98a00"/><use href="#star" x="62" fill="url(#starFill)" stroke="#c98a00"/><use href="#star" x="93" fill="url(#starEmpty)" stroke="#bbb"/><use href="#star" x="124" fill="url(#starEmpty)" stroke="#bbb"/></svg>
  <div class="formats"><svg width="48" height="32" viewBox="0 0 48 32"><use href="#people"/></svg></div>
  <svg class="badge" width="50" height="46" viewBox="0 0 50 46"><use href="#heart"/></svg>
  <p class="price">$995</p>
  <svg class="register-tab" width="146" height="36" viewBox="0 0 146 36"><use href="#registerTab"/><text x="73" y="24" text-anchor="middle" fill="#fff" font-size="18" font-family="Open Sans, Arial, sans-serif">Register</text></svg>
</article>

<article class="abs course-card" style="left:610px">
  <div class="provider-logo" style="font-size:15px"><span class="mark"></span>Harbourview<br>School of Business</div>
  <h3 class="course-title">Product Management<br>Focus</h3>
  <p class="course-provider">Meridian Marketing</p>
  <svg class="stars" width="150" height="24" viewBox="0 0 150 24"><use href="#star" fill="url(#starFill)" stroke="#c98a00"/><use href="#star" x="31" fill="url(#starFill)" stroke="#c98a00"/><use href="#star" x="62" fill="url(#starFill)" stroke="#c98a00"/><use href="#star" x="93" fill="url(#starEmpty)" stroke="#bbb"/><use href="#star" x="124" fill="url(#starEmpty)" stroke="#bbb"/></svg>
  <div class="formats"><svg width="48" height="32" viewBox="0 0 48 32"><use href="#people"/></svg></div>
  <svg class="badge" width="50" height="46" viewBox="0 0 50 46"><use href="#heart"/></svg>
  <p class="price" style="right:8px">$32,85</p>
  <svg class="register-tab" width="146" height="36" viewBox="0 0 146 36"><use href="#registerTab"/><text x="73" y="24" text-anchor="middle" fill="#fff" font-size="18" font-family="Open Sans, Arial, sans-serif">Register</text></svg>
</article>

<article class="abs course-card" style="left:865px">
  <div class="provider-logo"><span class="mark"></span>Meridian<br>Marketing</div>
  <h3 class="course-title">Product Management<br>Focus</h3>
  <p class="course-provider">Meridian Marketing</p>
  <svg class="stars" width="150" height="24" viewBox="0 0 150 24"><use href="#star" fill="url(#starFill)" stroke="#c98a00"/><use href="#star" x="31" fill="url(#starFill)" stroke="#c98a00"/><use href="#star" x="62" fill="url(#starFill)" stroke="#c98a00"/><use href="#star" x="93" fill="url(#starFill)" stroke="#c98a00"/><use href="#star" x="124" fill="url(#starEmpty)" stroke="#bbb"/></svg>
  <div class="formats" style="gap:12px">
    <svg width="36" height="34" viewBox="0 0 36 34"><rect x="6" y="1" width="28" height="32" rx="3" fill="#3c3c3c"/><rect x="2" y="7" width="8" height="4" rx="1" fill="#3c3c3c" stroke="#eee"/><rect x="2" y="15" width="8" height="4" rx="1" fill="#3c3c3c" stroke="#eee"/><rect x="2" y="23" width="8" height="4" rx="1" fill="#3c3c3c" stroke="#eee"/><path d="M16 10c2 0 3 3 3 4l-2 2c1 2 2 3 4 4l2-2c1 0 4 1 4 3 0 2-2 3-3 3-6 0-11-5-11-11 0-1 1-3 3-3z" fill="#fff"/></svg>
    <svg width="48" height="32" viewBox="0 0 48 32"><use href="#people"/></svg>
    <svg width="42" height="34" viewBox="0 0 42 34"><rect x="1" y="1" width="40" height="26" rx="2" fill="#3c3c3c"/><rect x="5" y="5" width="32" height="18" fill="#f4f4f4"/><rect x="15" y="27" width="12" height="4" fill="#3c3c3c"/><rect x="10" y="31" width="22" height="3" fill="#3c3c3c"/></svg>
  </div>
  <svg class="badge" width="40" height="34" viewBox="0 0 40 34" style="left:20px;top:242px"><path d="M2 18l6-6 8 8L33 2l6 6-23 24z" fill="var(--tick)" stroke="#3f7411" stroke-width="1"/></svg>
  <p class="price">$995</p>
  <svg class="register-tab" width="146" height="36" viewBox="0 0 146 36"><use href="#registerTab"/><text x="73" y="24" text-anchor="middle" fill="#fff" font-size="18" font-family="Open Sans, Arial, sans-serif">Register</text></svg>
</article>

</body>
</html>
```